Wirenexa

I'm looking to much improve our current website wirenexa.com
Updates

Low design quality

Target Market(s)

Commercial clients (Not-Residentials)

Industry/Entity Type

Office buildings and Industrial clients

Coding

Coded - Design and coding required

Number of Pages Required

5+ page

Requirements
Must have
• Very professional structured low voltage cabling projects for Wi-Fi, Audio/Video conference rooms, Access Control systems, CCTV.

```html
<!DOCTYPE html>
<html lang="en">
<head>
<meta charset="utf-8">
<title>Wirenexa — Structured Cabling for Commercial &amp; Industrial Buildings</title>
<link href="https://fonts.googleapis.com/css2?family=Inter:wght@400;500;600;700&display=swap" rel="stylesheet">
<style>
:root{
  --ink:#0f1b2d;
  --night:#0b1426;
  --navy:#1d3a6d;
  --orange:#e27d1c;
  --muted:#6b7588;
  --soft:#f5f7fb;
  --line:#e3e7ef;
  --chip:#e8eef8;
  --white:#ffffff;
}
*{box-sizing:border-box;margin:0;padding:0}
html,body{width:1200px;height:2599px;overflow:hidden}
body{font-family:'Inter',sans-serif;color:var(--ink);background:var(--white);font-size:13px}
.wrap{width:756px;margin:0 auto;position:relative}
a{color:inherit;text-decoration:none}

.topbar{height:27px;background:var(--night);color:#9aa4b8;font-size:11px;display:flex;justify-content:space-between;align-items:center;padding:0 23px}
.topbar .contact{color:var(--orange);font-weight:500;font-size:12px}

.nav{height:50px;display:flex;align-items:center;justify-content:space-between;padding:0 23px;border-bottom:1px solid var(--line)}
.brand{display:flex;align-items:center;gap:9px;font-weight:600;font-size:15px;color:var(--ink)}
.brand .mark{width:30px;height:30px;background:var(--navy);border-radius:5px}
.nav ul{display:flex;gap:25px;list-style:none;align-items:center;font-size:12px;color:#2b3446}
.btn-nav{background:var(--navy);color:#fff;padding:8px 15px;border-radius:4px;font-weight:500}

.hero{height:474px;background:var(--night);color:#fff}
.hero .wrap{display:flex;justify-content:space-between;padding-top:54px}
.hero-copy{width:360px}
.eyebrow-badge{display:inline-block;border:1px solid #8a4d14;background:#2a2013;color:var(--orange);font-size:10px;letter-spacing:1.5px;padding:4px 15px;border-radius:3px;font-weight:600}
.hero h1{font-size:31px;line-height:34px;font-weight:600;margin-top:15px;letter-spacing:-.3px}
.hero h1 span{color:var(--orange)}
.hero p{color:#b4bccb;font-size:12.5px;line-height:20px;margin-top:16px}
.hero-actions{display:flex;gap:9px;margin-top:20px}
.btn{display:inline-flex;align-items:center;justify-content:center;height:34px;padding:0 18px;border-radius:4px;font-size:12px;font-weight:500}
.btn-orange{background:var(--orange);color:#fff}
.btn-ghost{border:1px solid #5b6478;color:#fff}
.stats{display:flex;flex-wrap:wrap;gap:17px 17px;margin-top:22px;width:290px}
.stat{border-left:2px solid var(--orange);padding-left:10px;height:36px}
.stat b{display:block;font-size:18px;font-weight:500}
.stat small{display:block;font-size:9.5px;letter-spacing:1.2px;color:#8d97aa;margin-top:2px}
.callback{width:359px;height:338px;background:#fff;border-radius:8px;padding:20px 21px;color:var(--ink);margin-top:17px;margin-right:-1px}
.callback h2{font-size:13px;font-weight:600}
.callback .note{font-size:10.5px;color:var(--muted);margin-top:3px}
.field{height:30px;border:1px solid var(--line);background:#f8f9fc;border-radius:4px;margin-top:8px;font-size:11px;color:var(--muted);padding:8px 10px}
.field:first-of-type{margin-top:13px}
.field.tall{height:58px}
.send{height:30px;background:var(--navy);color:#fff;border-radius:4px;margin-top:8px;display:flex;align-items:center;justify-content:center;font-size:11.5px;font-weight:600}

.trust{height:40px;background:var(--navy);color:#d9e1ef;font-size:11px;display:flex;align-items:center;justify-content:center;gap:40px}

.section-soft{background:var(--soft)}
.eyebrow{color:var(--orange);font-size:10px;letter-spacing:2px;font-weight:600}
.section-title{font-size:22px;font-weight:600;margin-top:9px;letter-spacing:-.2px}
.lede{color:#4b5567;font-size:12.5px;line-height:20px;margin-top:9px;width:430px}

.services{height:599px;padding-top:46px}
.service-grid{display:grid;grid-template-columns:repeat(4,178px);gap:12px 12px;margin-top:29px}
.service{height:187px;background:#fff;border:1px solid var(--line);border-radius:6px;padding:19px 13px}
.service.active{border-top:3px solid var(--orange)}
.service .icon{width:33px;height:33px;background:var(--chip);border-radius:6px}
.service h3{font-size:12px;font-weight:600;margin-top:15px}
.service p{font-size:10.5px;line-height:16px;color:var(--muted);margin-top:6px}
.tag{display:inline-block;background:var(--chip);color:var(--navy);font-size:8.5px;letter-spacing:1px;font-weight:600;padding:3px 7px;border-radius:3px;margin-top:9px}

.why{height:376px;padding-top:47px}
.why .wrap{display:flex;justify-content:space-between}
.why-copy{width:365px}
.why-copy .lede{width:365px;font-size:13px;line-height:21px}
.checks{list-style:none;margin-top:16px;padding-left:9px}
.checks li{font-size:11.5px;line-height:22px;color:#2b3446}
.why-copy .btn{margin-top:17px;height:31px}
.why-grid{display:grid;grid-template-columns:repeat(2,176px);gap:12px;align-content:start}
.why-card{height:96px;background:var(--soft);border:1px solid var(--line);border-radius:6px;padding:15px 15px}
.why-card h3{font-size:11.5px;font-weight:600}
.why-card p{font-size:10.5px;line-height:16px;color:var(--muted);margin-top:5px}

.industries{height:304px;padding-top:47px}
.industry-grid{display:grid;grid-template-columns:repeat(3,242px);gap:12px;margin-top:15px}
.industry{background:#fff;border:1px solid var(--line);border-radius:6px;overflow:hidden;height:158px}
.industry h3{background:var(--navy);color:#fff;font-size:12px;font-weight:500;height:44px;display:flex;align-items:center;padding:0 22px}
.industry ul{list-style:none;padding:13px 12px}
.industry li{font-size:10.5px;line-height:18.4px;color:#3c4556;display:flex;align-items:center;gap:7px}
.industry li::before{content:"";width:4px;height:4px;border-radius:50%;background:var(--orange)}

.process{height:282px;padding-top:47px;text-align:center}
.process .section-title{margin-top:8px}
.steps{display:grid;grid-template-columns:repeat(4,188px);margin:21px 0 0 -8px;position:relative;width:752px}
.steps::before{content:"";position:absolute;left:94px;right:94px;top:23px;height:1px;background:var(--line)}
.step{position:relative}
.step .num{width:47px;height:47px;border-radius:50%;background:var(--navy);color:#fff;font-size:14px;display:flex;align-items:center;justify-content:center;margin:0 auto;border:3px solid #fff;box-shadow:0 0 0 1px #d9dfea}
.step h3{font-size:11.5px;font-weight:600;margin-top:13px}
.step p{font-size:9.5px;line-height:14px;color:var(--muted);margin-top:4px;padding:0 4px}

.cta{height:202px;background:var(--night);color:#fff;text-align:center;padding-top:46px}
.cta h2{font-size:23px;font-weight:600}
.cta p{color:#9aa4b8;font-size:12.5px;margin-top:10px}
.cta-actions{display:flex;gap:10px;justify-content:center;margin-top:21px}
.cta .btn{height:37px;font-size:13px;padding:0 27px}
.cta .btn-orange{width:137px}
.cta .btn-ghost{width:175px}

.footer{height:245px;background:var(--night);border-top:1px solid #17213a;color:#8d97aa;padding-top:38px}
.footer-cols{display:flex}
.footer-about{width:294px}
.footer-about .brand-name{color:#fff;font-size:14px;font-weight:600}
.footer-about p{font-size:10.5px;line-height:17px;margin-top:9px;width:170px}
.footer-col{width:159px}
.footer-col h4{font-size:9px;letter-spacing:1.6px;font-weight:600;color:#6f7a8f}
.footer-col ul{list-style:none;margin-top:9px}
.footer-col li{font-size:10.5px;line-height:19.2px;color:#b4bccb}
.footer-bottom{display:flex;justify-content:space-between;border-top:1px solid #1c2740;margin-top:28px;padding-top:11px;font-size:9.5px;color:#6f7a8f}
.footer-bottom span+span{margin-left:16px}
</style>
</head>
<body>

<div class="topbar">
  <span>Serving Virginia · Washington DC · Maryland</span>
  <span class="contact">(888) 555-0142 · sales@wirenexa.com</span>
</div>

<header class="nav">
  <a class="brand" href="#"><span class="mark"></span>Wirenexa</a>
  <ul>
    <li>Services</li><li>Industries</li><li>Projects</li><li>About</li>
    <li><a class="btn-nav" href="#">Request a Quote</a></li>
  </ul>
</header>

<section class="hero">
  <div class="wrap">
    <div class="hero-copy">
      <span class="eyebrow-badge">CERTIFIED LOW VOLTAGE CONTRACTOR</span>
      <h1>Structured Cabling for <span>Commercial &amp; Industrial</span> Buildings</h1>
      <p>Wi-Fi infrastructure, AV conference rooms, access control, and CCTV — engineered, installed, and certified for office buildings, data centers, and warehouses across the DMV.</p>
      <div class="hero-actions">
        <a class="btn btn-orange" href="#">Get a Free Quote</a>
        <a class="btn btn-ghost" href="#">View Our Services</a>
      </div>
      <div class="stats">
        <div class="stat"><b>15+</b><small>YEARS EXPERIENCE</small></div>
        <div class="stat"><b>500+</b><small>PROJECTS COMPLETED</small></div>
        <div class="stat"><b>3</b><small>STATES SERVED</small></div>
      </div>
    </div>
    <form class="callback">
      <h2>Request a Callback</h2>
      <p class="note">We respond within 1 business hour.</p>
      <div class="field">Full name</div>
      <div class="field">Company name</div>
      <div class="field">Work email</div>
      <div class="field">Phone number</div>
      <div class="field tall">Describe your project or request...</div>
      <div class="send">Send Request →</div>
    </form>
  </div>
</section>

<div class="trust">
  <span>Veritest VX-8000 Certified</span>
  <span>Licensed &amp; Insured</span>
  <span>5-Star Verified Reviews</span>
  <span>Commercial &amp; Industrial</span>
  <span>24/7 Support Available</span>
</div>

<section class="services section-soft">
  <div class="wrap">
    <div class="eyebrow">WHAT WE DO</div>
    <h2 class="section-title">Complete Low Voltage Solutions</h2>
    <p class="lede">From initial design through certification testing, we deliver turnkey structured cabling for every system your facility needs.</p>
    <div class="service-grid">
      <article class="service active"><div class="icon"></div><h3>Wi-Fi Infrastructure</h3><p>Enterprise wireless design, AP placement surveys, and full deployment for offices and warehouses.</p><span class="tag">CAT6 · CAT6A</span></article>
      <article class="service"><div class="icon"></div><h3>AV Conference Rooms</h3><p>Audio/video cabling and infrastructure for boardrooms, huddle spaces, and training rooms.</p><span class="tag">HDMI · SPEAKER</span></article>
      <article class="service"><div class="icon"></div><h3>Access Control</h3><p>Card readers, door controllers, and intercom cabling for secure entry systems.</p><span class="tag">RS-485 · IP</span></article>
      <article class="service"><div class="icon"></div><h3>CCTV / IP Cameras</h3><p>PoE camera cabling, NVR infrastructure, and conduit runs for full-coverage surveillance.</p><span class="tag">POE · FIBER</span></article>
      <article class="service"><div class="icon"></div><h3>IDF / MDF Rooms</h3><p>Rack installation, patch panel termination, and structured pathway builds for data rooms.</p><span class="tag">CAT6 · FIBER</span></article>
      <article class="service"><div class="icon"></div><h3>Fiber Optic</h3><p>Single and multimode fiber runs for high-bandwidth inter-building and backbone connections.</p><span class="tag">SM · MM · OS2</span></article>
    </div>
  </div>
</section>

<section class="why">
  <div class="wrap">
    <div class="why-copy">
      <div class="eyebrow">WHY WIRENEXA</div>
      <h2 class="section-title">Built for commercial-grade projects</h2>
      <p class="lede">We work directly with IT managers, general contractors, and facilities teams to keep projects on spec, on schedule, and within budget.</p>
      <ul class="checks">
        <li>Certified Veritest VX-8000 testing on every run</li>
        <li>Full as-built documentation provided post-install</li>
        <li>Coordination with your IT staff and GC</li>
        <li>After-hours and weekend installs available</li>
        <li>Warranty on materials and workmanship</li>
      </ul>
      <a class="btn btn-orange" href="#">See Our Work →</a>
    </div>
    <div class="why-grid">
      <div class="why-card"><h3>On-time delivery</h3><p>Structured scheduling and a dedicated PM on every project over 50 drops.</p></div>
      <div class="why-card"><h3>Certified testing</h3><p>Every cable run passes Veritest VX-8000 Cat6/6A certification before sign-off.</p></div>
      <div class="why-card"><h3>Full documentation</h3><p>Label maps, test reports, and CAD-ready diagrams delivered at completion.</p></div>
      <div class="why-card"><h3>Post-install support</h3><p>We stay available after the job. Moves, adds, and changes handled quickly.</p></div>
    </div>
  </div>
</section>

<section class="industries section-soft">
  <div class="wrap">
    <div class="eyebrow">INDUSTRIES SERVED</div>
    <h2 class="section-title">Expertise across commercial sectors</h2>
    <div class="industry-grid">
      <div class="industry"><h3>Office Buildings</h3><ul><li>Multi-floor structured cabling</li><li>Conference room AV systems</li><li>Wireless access point deployment</li><li>Access control and intercom</li><li>IDF/MDF room buildouts</li></ul></div>
      <div class="industry"><h3>Industrial &amp; Warehouses</h3><ul><li>High-bay Wi-Fi coverage</li><li>Conduit and cable tray runs</li><li>IP camera and CCTV systems</li><li>Outdoor-rated cabling</li><li>Fiber backbone installations</li></ul></div>
      <div class="industry"><h3>Healthcare &amp; Education</h3><ul><li>HIPAA-compliant network cabling</li><li>Nurse call and PA systems</li><li>Classroom AV infrastructure</li><li>Campus fiber optic backbone</li><li>Badge access and CCTV</li></ul></div>
    </div>
  </div>
</section>

<section class="process">
  <div class="wrap">
    <div class="eyebrow">HOW IT WORKS</div>
    <h2 class="section-title">From quote to certification in 4 steps</h2>
    <div class="steps">
      <div class="step"><div class="num">1</div><h3>Site Survey</h3><p>We assess your facility and document scope, pathways, and requirements.</p></div>
      <div class="step"><div class="num">2</div><h3>Design &amp; Quote</h3><p>Detailed proposal with materials, labor, and timeline — no surprises.</p></div>
      <div class="step"><div class="num">3</div><h3>Installation</h3><p>Clean, labeled, industry-standard installation by our certified technicians.</p></div>
      <div class="step"><div class="num">4</div><h3>Test &amp; Sign-off</h3><p>Veritest-certified testing, documentation package, and walk-through with your team.</p></div>
    </div>
  </div>
</section>

<section class="cta">
  <h2>Ready to plan your next cabling project?</h2>
  <p>Talk to a low voltage specialist — free site assessment available for commercial projects in VA, DC, and MD.</p>
  <div class="cta-actions">
    <a class="btn btn-orange" href="#">(888) 555-0142</a>
    <a class="btn btn-ghost" href="#">sales@wirenexa.com</a>
  </div>
</section>

<footer class="footer">
  <div class="wrap">
    <div class="footer-cols">
      <div class="footer-about">
        <div class="brand-name">Wirenexa</div>
        <p>Professional low voltage cabling contractor serving Virginia, Washington DC, and Maryland since 2009. Licensed, insured, and Veritest-certified.</p>
      </div>
      <div class="footer-col"><h4>SERVICES</h4><ul><li>Wi-Fi Infrastructure</li><li>AV Conference Rooms</li><li>Access Control</li><li>CCTV / IP Cameras</li><li>Fiber Optic</li><li>IDF / MDF Rooms</li></ul></div>
      <div class="footer-col"><h4>INDUSTRIES</h4><ul><li>Office Buildings</li><li>Industrial / Warehouse</li><li>Healthcare</li><li>Education</li><li>Data Centers</li></ul></div>
      <div class="footer-col"><h4>COMPANY</h4><ul><li>About Us</li><li>Projects</li><li>Contact</li><li>Request a Quote</li><li>703-555-0187</li></ul></div>
    </div>
    <div class="footer-bottom">
      <span>© 2026 Wirenexa · 4100 Harbor Point Dr, Suite 310, Fairfax, VA 22030</span>
      <div><span>(888) 555-0142</span><span>sales@wirenexa.com</span></div>
    </div>
  </div>
</footer>

</body>
</html>
```